Web Design

Looking for web designer for total service. We would like to make it in English and Japanese for now. Also need to make Tablet version. Our website is www.brindlecove.com and www.quartzmeadow .com

```html
<!DOCTYPE html>
<html lang="en">
<head>
<meta charset="utf-8">
<title>Brindle Cove — Delicious Food</title>
<link rel="stylesheet" href="https://fonts.googleapis.com/css2?family=Montserrat:wght@400;500;600;700&family=Open+Sans:wght@400;600;700&family=Dancing+Script:wght@400;600&display=swap">
<style>
:root{
  --green:#3aae3f;
  --green-dark:#2c8f32;
  --lime:#8cc63f;
  --ink:#3b3b3b;
  --muted:#8a8f95;
  --heading-grey:#a3a9ae;
  --paper:#f3f3f3;
  --paper-2:#e9e9e9;
  --white:#ffffff;
  --slate:#5e6570;
  --slate-dark:#555c66;
  --line:#d9dcdf;
}
*{box-sizing:border-box;margin:0;padding:0}
html,body{width:1200px;height:4027px;overflow:hidden}
body{position:relative;background:var(--white);font-family:"Open Sans",sans-serif;color:var(--ink)}
.abs{position:absolute}
.ph{position:absolute}
.script{font-family:"Dancing Script",cursive;font-weight:400;color:#2f2f2f}

/* header */
.site-header{position:absolute;top:0;left:0;width:1200px;height:56px;background:var(--white);border-bottom:1px solid #ececec;z-index:3}
.nav-link{position:absolute;top:22px;font-family:"Montserrat",sans-serif;font-size:13px;color:#6c7177}
.nav-link.active{color:#444}
.nav-link.active::before{content:"";position:absolute;left:0;right:0;top:-22px;height:3px;background:var(--lime)}
.brand-tab{position:absolute;left:558px;top:0;width:86px;height:106px;background:var(--white);box-shadow:0 2px 6px rgba(0,0,0,.12);display:flex;align-items:center;justify-content:center;text-align:center;z-index:4}
.brand-tab span{font-family:"Montserrat",sans-serif;font-weight:600;font-size:14px;line-height:17px;color:var(--green-dark)}
.cart{position:absolute;left:938px;top:18px;font-family:"Montserrat",sans-serif;font-weight:700;font-size:12px;color:#333;line-height:13px}
.cart small{display:block;font-weight:500;font-size:10px;color:var(--lime);text-align:right}

/* hero */
.hero{position:absolute;top:0;left:0;width:1200px;height:604px;background:linear-gradient(180deg,#f1f1f1,#e6e6e6)}
.hero h1{position:absolute;top:134px;left:0;width:1200px;text-align:center;font-family:"Montserrat",sans-serif;font-weight:600;font-size:34px;line-height:38px;letter-spacing:2px;color:var(--heading-grey)}
.hero .lead{position:absolute;top:224px;left:300px;width:600px;text-align:center;font-size:15px;line-height:23px;color:#999}
.hero .tag{position:absolute;left:148px;top:304px;font-size:27px;line-height:26px;color:var(--lime);transform:rotate(-6deg)}
.hero .price{position:absolute;left:440px;top:308px;font-size:32px;color:#8a8a8a}
.btn-outline{position:absolute;border:2px solid #cfd3d6;border-radius:24px;background:transparent;font-family:"Montserrat",sans-serif;font-weight:500;color:#777;text-align:center}
.hero .btn-outline{left:572px;top:306px;width:180px;height:46px;line-height:42px;font-size:14px}

/* about */
.about{position:absolute;top:604px;left:0;width:1200px;height:537px;background:linear-gradient(180deg,#fafafa,#f4f4f4)}
.about h2{position:absolute;left:160px;top:94px;font-size:40px}
.about p{position:absolute;left:161px;width:510px;font-size:13px;line-height:23px;color:#444}
.photo-card{position:absolute;background:var(--white);padding:6px;box-shadow:0 2px 8px rgba(0,0,0,.2)}
.photo-card .ph{position:static;width:100%;height:100%}

/* process */
.process{position:absolute;top:1141px;left:0;width:1200px;height:301px;background:linear-gradient(180deg,#3fb545,#34a53a);color:var(--white);text-align:center}
.process h2{position:absolute;top:30px;width:1200px;font-family:"Montserrat",sans-serif;font-weight:400;font-size:32px}
.process p{position:absolute;top:90px;left:210px;width:780px;font-size:13px;font-weight:700;line-height:22px}
.pill{position:absolute;top:204px;width:153px;height:40px;border-radius:22px;font-family:"Montserrat",sans-serif;font-weight:700;font-size:10px;line-height:40px;text-align:center}
.pill.dark{left:438px;background:var(--green-dark);color:var(--white)}
.pill.light{left:615px;background:var(--white);color:var(--green-dark)}

/* products */
.products{position:absolute;top:1442px;left:0;width:1200px;height:679px;background:var(--white)}
.section-title{position:absolute;left:0;width:1200px;text-align:center;font-size:38px}
.product-card{position:absolute;top:282px;width:269px;height:258px;background:var(--white);box-shadow:0 1px 8px rgba(0,0,0,.18);text-align:center}
.product-card .shade{position:absolute;left:14px;top:12px;right:14px;bottom:12px;background:#f3f3f3}
.product-card .cost{position:relative;margin-top:26px;font-family:"Montserrat",sans-serif;font-size:22px;color:var(--lime)}
.product-card .desc{position:relative;margin-top:6px;font-size:17px;line-height:22px;color:#555}
.product-card .btn-outline{left:64px;top:198px;width:141px;height:34px;line-height:30px;font-size:10px}
.btn-solid{position:absolute;background:var(--green);color:var(--white);font-family:"Montserrat",sans-serif;font-weight:700;text-align:center;border-radius:22px}

/* testimonials */
.testimonials{position:absolute;top:2148px;left:0;width:1200px;height:443px;background:linear-gradient(180deg,#f1f1f1,#e8e8e8)}
.testimonials .pager{position:absolute;top:156px;font-family:"Montserrat",sans-serif;font-size:17px;display:flex;align-items:center;gap:10px}
.avatar{position:absolute;top:113px;width:140px;height:120px;background:var(--white);padding:5px;box-shadow:0 2px 6px rgba(0,0,0,.25)}
.avatar .ph{position:static;width:100%;height:100%}
.person{position:absolute;top:248px;width:140px;text-align:center;font-size:12px;font-weight:700;color:#888}
.testimonials blockquote{position:absolute;top:282px;left:248px;width:704px;text-align:center;font-size:13px;line-height:23px;color:#444}
.dots{position:absolute;top:404px;left:560px;display:flex;gap:8px}
.dots i{width:7px;height:7px;border-radius:50%;background:#cfd3d6}
.dots i.on{background:var(--lime)}

/* articles */
.articles{position:absolute;top:2591px;left:0;width:1200px;height:532px;background:var(--white)}
.article{position:absolute;top:121px;width:273px;height:336px;background:var(--white);box-shadow:0 1px 7px rgba(0,0,0,.2)}
.article .ph{position:static;width:100%;height:180px}
.article h3{margin:20px 10px 0;font-size:13px;font-weight:700;color:#333}
.article p{margin:6px 10px 0;font-size:10px;line-height:14px;color:#444}
.article .more{position:absolute;left:10px;bottom:24px;font-size:12px;font-weight:700;color:var(--lime)}
.carousel-arrow{position:absolute;top:268px;width:36px;height:36px;border-radius:50%;background:var(--white);box-shadow:0 1px 5px rgba(0,0,0,.2);display:flex;align-items:center;justify-content:center}

/* newsletter */
.newsletter{position:absolute;top:3123px;left:0;width:1200px;height:327px;background:linear-gradient(180deg,#f6f6f6,#ececec)}
.newsletter h2{position:absolute;top:62px;width:1200px;text-align:center;font-family:"Montserrat",sans-serif;font-weight:400;font-size:30px;color:#333}
.newsletter p{position:absolute;top:106px;left:420px;width:360px;text-align:center;font-size:16px;line-height:22px;color:#777}
.email-field{position:absolute;left:322px;top:185px;width:551px;height:56px;background:var(--white);border-radius:30px;box-shadow:0 1px 6px rgba(0,0,0,.12);font-size:16px;color:#aaa;line-height:56px;padding-left:32px}
.email-field svg{position:absolute;right:28px;top:20px}

/* contact */
.contact{position:absolute;top:3450px;left:0;width:1200px;height:416px;background:linear-gradient(180deg,var(--slate),var(--slate-dark));color:var(--white)}
.contact h2{position:absolute;top:64px;width:1200px;text-align:center;font-size:46px;color:var(--white)}
.field{position:absolute;border-bottom:1px solid rgba(255,255,255,.7);font-size:13px;font-weight:600;padding-bottom:8px}
.agree{position:absolute;left:244px;top:290px;font-size:11px;display:flex;align-items:center;gap:8px}
.agree i{width:14px;height:14px;background:var(--white);display:block}
.reply{position:absolute;left:728px;top:285px;font-size:11px;font-weight:600;line-height:14px;text-align:right;width:76px}
.contact .btn-solid{left:814px;top:285px;width:147px;height:35px;line-height:35px;font-size:11px;border-radius:3px;background:var(--lime)}

/* footer */
.site-footer{position:absolute;top:3866px;left:0;width:1200px;height:161px;background:var(--slate-dark);color:var(--white)}
.footer-brand{position:absolute;left:140px;top:22px;width:120px;text-align:center;font-family:"Montserrat",sans-serif;font-weight:600;font-size:18px;line-height:22px}
.footer-col{position:absolute;top:10px;font-size:10px;line-height:17px}
.footer-col h4{font-size:12px;font-weight:700;margin-bottom:4px}
</style>
</head>
<body>

<!-- Header -->
<header class="site-header">
  <a class="nav-link" style="left:190px">About us</a>
  <a class="nav-link active" style="left:290px">Contact us</a>
  <a class="nav-link" style="left:398px">Our Products</a>
  <a class="nav-link" style="left:718px">Online Shopping</a>
  <a class="nav-link" style="left:866px">Login</a>
  <div class="cart">Shopping cart<small>0 items</small></div>
</header>
<div class="brand-tab"><span>Brindle<br>Cove</span></div>

<!-- Hero -->
<section class="hero">
  <div class="ph" role="img" aria-label="Lemon half" style="left:0;top:0;width:60px;height:62px;border-radius:0 0 60px 0;background:radial-gradient(circle at 20% 20%,#ffe34d,#f3c813)"></div>
  <div class="ph" role="img" aria-label="Green apple" style="left:992px;top:148px;width:94px;height:120px;border-radius:46px;background:radial-gradient(circle at 40% 40%,#a5e04a,#5aa82a)"></div>
  <h1>DELICIOUS FOOD<br>WITH TRULLY FRESH INGREDIENTS</h1>
  <p class="lead">Only fresh and delicious food for you and your family with amazing strength and energy injection</p>
  <div class="tag script">Only Fresh<br>Products!</div>
  <svg class="abs" style="left:250px;top:334px" width="90" height="40" viewBox="0 0 90 40"><path d="M2 8 Q40 38 84 30" fill="none" stroke="#8cc63f" stroke-width="2"/><path d="M76 24 L85 30 L76 36" fill="none" stroke="#8cc63f" stroke-width="2"/></svg>
  <div class="price script">From $2.99</div>
  <a class="btn-outline">BUY NOW</a>
  <div class="ph" role="img" aria-label="Four pancake mix packages in a row" style="left:357px;top:376px;width:489px;height:228px;background:linear-gradient(90deg,#c9a777 0 22%,transparent 22% 26%,#e8a7b5 26% 48%,transparent 48% 52%,#c9a777 52% 74%,transparent 74% 78%,#c9a777 78%)"></div>
</section>

<!-- About -->
<section class="about">
  <h2 class="script">About us!</h2>
  <p style="top:167px">Lorem ipsum dolor sit amet, consectetuer adipiscing elit. Aenean commodo ligula eget dolor. Aenean massa. Cum sociis natoque penatibus et magnis dis parturient montes, nascetur ridiculus mus. Donec quam felis, ultricies nec, pellentesque eu, pretium quis, sem. Nulla consequat massa quis enim. Donec pede justo, fringilla vel, aliquet nec, vulputate eget, arcu.</p>
  <p style="top:349px">Lorem ipsum dolor sit amet, consectetuer adipiscing elit. Aenean commodo ligula eget dolor. Aenean massa. Cum sociis natoque penatibus et magnis.</p>
  <div class="photo-card" style="left:849px;top:94px;width:193px;height:145px"><div class="ph" role="img" aria-label="Shop interior" style="background:linear-gradient(135deg,#5a2f2a,#c9533c)"></div></div>
  <div class="photo-card" style="left:679px;top:146px;width:290px;height:204px"><div class="ph" role="img" aria-label="Pancake mix packages on a table" style="background:linear-gradient(135deg,#c64a3a,#d9a27a)"></div></div>
  <div class="photo-card" style="left:853px;top:296px;width:189px;height:128px"><div class="ph" role="img" aria-label="Jars of jam" style="background:linear-gradient(135deg,#d6a85a,#b26a3a)"></div></div>
</section>

<!-- Process -->
<section class="process">
  <h2>The Process of Making</h2>
  <p>Lorem ipsum dolor sit amet, consectetuer adipiscing elit. Aenean commodo ligula eget dolor. Aenean massa. Cum sociis natoque penatibus et magnis dis parturient montes, nascetur ridiculus mus. Donec quam felis, ultricies nec, pellentesque eu, pretium quis, sem. Nulla consequat</p>
  <a class="pill dark">BROWNIES DIET</a>
  <a class="pill light">ADVANCED DIET</a>
</section>

<!-- Selected products -->
<section class="products">
  <div class="ph" role="img" aria-label="Strawberry" style="left:96px;top:70px;width:40px;height:44px;border-radius:50% 50% 50% 50%/40% 40% 60% 60%;background:radial-gradient(circle at 40% 40%,#f04a4a,#c11d1d)"></div>
  <div class="ph" role="img" aria-label="Lemon" style="left:1066px;top:162px;width:98px;height:78px;border-radius:50%;background:radial-gradient(circle at 40% 40%,#ffe84d,#f2c511)"></div>
  <div class="ph" role="img" aria-label="Lemon" style="left:96px;top:492px;width:70px;height:56px;border-radius:50%;background:radial-gradient(circle at 40% 40%,#ffe84d,#f2c511)"></div>
  <h2 class="section-title script" style="top:52px">Selected products</h2>

  <div class="product-card" style="left:126px"><div class="shade"></div><div class="cost" style="margin-top:76px">$7,99</div><div class="desc">Your choice what text<br>to write here</div><a class="btn-outline">BUY NOW</a></div>
  <div class="product-card" style="left:475px"><div class="shade"></div><div class="cost" style="margin-top:76px">$19,99</div><div class="desc">Your choice what text<br>to write here</div><a class="btn-outline">BUY NOW</a></div>
  <div class="product-card" style="left:806px"><div class="shade"></div><div class="cost" style="margin-top:76px">$12,99</div><div class="desc">Your choice what text<br>to write here</div><a class="btn-outline">BUY NOW</a></div>

  <div class="ph" role="img" aria-label="Single pancake mix package" style="left:214px;top:161px;width:92px;height:196px;background:linear-gradient(180deg,#c9a777,#d7e7a0)"></div>
  <div class="ph" role="img" aria-label="Three pancake mix packages" style="left:510px;top:161px;width:200px;height:196px;background:linear-gradient(90deg,#c9d98a 0 33%,#e8a7b5 33% 66%,#c9d98a 66%)"></div>
  <div class="ph" role="img" aria-label="Two pancake mix packages" style="left:880px;top:161px;width:140px;height:196px;background:linear-gradient(90deg,#c9d98a 0 50%,#e8a7b5 50%)"></div>

  <a class="btn-solid" style="left:526px;top:600px;width:148px;height:38px;line-height:38px;font-size:10px">SHOW ALL</a>
</section>

<!-- Testimonials -->
<section class="testimonials">
  <h2 class="section-title script" style="top:38px;font-size:34px">Testimonials</h2>
  <div class="pager" style="left:263px;color:#555"><svg width="26" height="14" viewBox="0 0 26 14"><path d="M25 7H2M8 1L2 7l6 6" fill="none" stroke="#555" stroke-width="2"/></svg>Previous</div>
  <div class="pager" style="left:814px;color:#b4b8bc">Next one<svg width="26" height="14" viewBox="0 0 26 14"><path d="M1 7h23M18 1l6 6-6 6" fill="none" stroke="#b4b8bc" stroke-width="2"/></svg></div>
  <div class="avatar" style="left:456px;transform:rotate(-3deg)"><div class="ph" role="img" aria-label="Customer portrait" style="background:linear-gradient(135deg,#c9b28a,#7b6a4e)"></div></div>
  <div class="avatar" style="left:622px;transform:rotate(2deg)"><div class="ph" role="img" aria-label="Customer portrait" style="background:linear-gradient(135deg,#c13a2e,#5a2a24)"></div></div>
  <div class="person" style="left:456px">Mara Toll</div>
  <div class="person" style="left:622px">Dean Hollis</div>
  <blockquote>Lorem ipsum dolor sit amet, consectetuer adipiscing elit. Aenean commodo ligula eget dolor. Aenean massa. Cum sociis natoque penatibus et magnis dis parturient montes, nascetur ridiculus mus. Donec quam felis, ultricies nec, pellentesque eu, pretium quis, sem. Nulla consequat massa quis enim. Donec pede justo, fringilla vel, aliquet nec, vulputate eget, arcu. In enim justo, rhoncus ut,</blockquote>
  <div class="dots"><i></i><i class="on"></i><i></i><i></i><i></i><i></i></div>
</section>

<!-- Articles -->
<section class="articles">
  <h2 class="section-title script" style="top:46px;font-size:34px">Get smarter</h2>
  <div class="carousel-arrow" style="left:68px"><svg width="10" height="12" viewBox="0 0 10 12"><path d="M7 1L2 6l5 5" fill="none" stroke="#888" stroke-width="2"/></svg></div>
  <div class="carousel-arrow" style="left:1094px"><svg width="10" height="12" viewBox="0 0 10 12"><path d="M3 1l5 5-5 5" fill="none" stroke="#888" stroke-width="2"/></svg></div>
  <article class="article" style="left:166px">
    <div class="ph" role="img" aria-label="Café counter with drinks and flowers" style="background:linear-gradient(135deg,#3c4a3a,#b7392f)"></div>
    <h3>Title of the Arcticle</h3>
    <p>Lorem ipsum dolor sit amet, consectetuer adipiscing elit. Aenean commodo ligula eget dolor. Aenean massa. Cum sociis natoque penatibus et magnis dis parturient montes.</p>
    <a class="more">Read More</a>
  </article>
  <article class="article" style="left:465px">
    <div class="ph" role="img" aria-label="Bowl of noodle soup" style="background:radial-gradient(circle,#f3b54a,#d5862b 60%,#8a5a2a)"></div>
    <h3>Title of the Arcticle</h3>
    <p>Lorem ipsum dolor sit amet, consectetuer adipiscing elit. Aenean commodo ligula eget dolor. Aenean massa. Cum sociis natoque penatibus et magnis dis parturient montes.</p>
    <a class="more">Read More</a>
  </article>
  <article class="article" style="left:765px">
    <div class="ph" role="img" aria-label="People talking at a table" style="background:linear-gradient(135deg,#9fc3d9,#3d6e9a)"></div>
    <h3>Title of the Arcticle</h3>
    <p>Lorem ipsum dolor sit amet, consectetuer adipiscing elit. Aenean commodo ligula eget dolor. Aenean massa. Cum sociis natoque penatibus et magnis dis parturient montes.</p>
    <a class="more">Read More</a>
  </article>
</section>

<!-- Newsletter -->
<section class="newsletter">
  <div class="ph" role="img" aria-label="Three pancake mix packages" style="left:54px;top:153px;width:174px;height:188px;background:linear-gradient(90deg,#c9d98a 0 33%,#e8a7b5 33% 66%,#c9d98a 66%)"></div>
  <h2>Subscribe to our newsletter</h2>
  <p>Lorem ipsum dolor sit amet, consec scing elit commodo ligula.</p>
  <div class="email-field">Your email address here..
    <svg width="24" height="16" viewBox="0 0 24 16"><rect width="24" height="16" rx="2" fill="#8cc63f"/><path d="M2 2l10 7 10-7" fill="none" stroke="#fff" stroke-width="2"/></svg>
  </div>
</section>

<!-- Contact -->
<section class="contact">
  <h2 class="script">Get in touch</h2>
  <div class="field" style="left:244px;top:170px;width:341px">Your Full Name...</div>
  <div class="field" style="left:615px;top:170px;width:343px">Your Email Address...</div>
  <div class="field" style="left:244px;top:233px;width:714px">Write a message for us...</div>
  <div class="agree"><i></i>I understand</div>
  <div class="reply">We will answer in 24hours</div>
  <a class="btn-solid">SEND A MESSAGE</a>
</section>

<!-- Footer -->
<footer class="site-footer">
  <div class="footer-brand">Brindle<br>Cove</div>
  <div class="footer-col" style="left:384px"><h4>Navigation</h4>How it Works<br>Pricing Page<br>Try Our Tools<br>Sign Up<br>Login</div>
  <div class="footer-col" style="left:550px"><h4>Policy</h4>Conditions &amp; Terms<br>About us<br>Privacy Policy<br>Write to us<br>Store Security</div>
  <div class="footer-col" style="left:744px"><h4>Contacts</h4>Street Address<br>Phone Numbers<br>Email Addresses<br>Working Hours<br>Products</div>
  <div class="footer-col" style="left:926px"><h4>Social</h4>Follow us<br>Updates<br>Journal</div>
</footer>

</body>
</html>
```